Doctor Formulated Medical Cosmetics

Halvessa Rue is an E-commerce site for high end Medical Cosmetics designed to treat specific skin problems. The Halvessa Rue difference/advantage is that all creams and serums are:
Doctor Formulated, Freshly Handmade, Registered Pharmacy.
The Site also provides real doctor Dermatology Consultations, Library (with a list of - 1. Active Ingredients in the creams with description of their effects, 2. Skin Conditions with information on what causes the condition and typical treatment approaches and outcomes. 3. Resources from Dermatology Journals and literature on the conditions.)
Header Information: Halvessa Rue, languages EN, BG, Register / log in, Shopping Bag. This field should be narrow.
Categories (horizontal): Home, Face, Body, Hair Care, Skin Conditions, Doctor Consultation, Library
The Landing Page should have only one well organized picture, which is intended to create the feeling of luxury, freedom and relaxation. It will be large and will fill the whole screen. All text should be on transparent or similar color fields. Please use the color of the text to create also the feeling of conservative luxury.
Written message / image overlay Halvessa Rue(logo), Skin Care, Doctor Formulated, Freshly Handmade, Registered Pharmacy.
Please study the Landing Page of this site as an example: www.marivelta.com
Under the Landing Page, there should be a slider with 4 of our products.
Underneath: Four Blog Articles (large pictures for maximum impact and luxury text underneath).
Underneath: Banner for Dermatologist Consultation, (button for Start Your Case Now).
Underneath: Two pictures in a line - Library (with books), and Active Ingredients.
Footer: Philosophy, Categories, Customer Care
Please adhere to the color palate provided in the pictures (as attachments). Provided are some examples of Web Sites with the desired look and feel. www.quillon.com , www.tavishrowe.com .
Please use different shades of gray, white, beige and gold colors, and black. Our products will be in brown glass jars and bottles to convey the professional, pharmacy made nature of the creams and lotions.
We find the following Front Page very attractive and effective - www.marivelta.com , with its full page image and overlaying text.
Please have a look at this link for the Landing page.
http://www.framstockly.com/detail/video/woman-lying-on-a-black-sand-beach-in-a-bikini-stock-footage/31862074
I would like to use it in the animated version to achieve the WOW effect. I have uploaded the jpeg version for it, so you will be able create your design.
For the Landing page design, please use only the two uploaded pictures of a woman laying at the beach. Let's see how each of them will look like.
Thank you for your help.

```html
<!DOCTYPE html>
<html lang="en">
<head>
<meta charset="utf-8">
<title>Halvessa Rue — Doctor Formulated Medical Cosmetics</title>
<link href="https://fonts.googleapis.com/css2?family=Montserrat:wght@400;600;700&family=Open+Sans:wght@400;600&family=Raleway:wght@300;400;600&display=swap" rel="stylesheet">
<style>
:root{
  --topbar:#9a8c82;
  --gold:#d3a656;
  --gold-deep:#c79a4a;
  --ink:#333333;
  --muted:#8a8a8a;
  --white:#ffffff;
  --footer:#2e2d2d;
  --footer-line:#4a4848;
  --caption:rgba(255,255,255,0.86);
}
*{margin:0;padding:0;box-sizing:border-box}
html,body{width:1200px;height:3564px;overflow:hidden;background:var(--white)}
body{position:relative;font-family:"Open Sans",Arial,sans-serif;color:var(--ink)}
.abs{position:absolute}

/* top bar */
.topbar{left:0;top:0;width:1200px;height:40px;background:var(--topbar);font-family:"Montserrat",Arial,sans-serif;font-size:11px;color:var(--white);font-weight:600}
.topbar .flag{left:171px;top:14px;width:22px;height:13px;background:linear-gradient(135deg,#24377a 0 40%,#c8202f 40% 60%,#24377a 60%)}
.topbar .lang-caret{left:198px;top:18px;width:0;height:0;border-left:3px solid transparent;border-right:3px solid transparent;border-top:4px solid var(--white)}
.topbar .site-name{left:240px;top:13px;font-weight:400}
.topbar .login{left:815px;top:13px}
.topbar .register{left:893px;top:13px;font-weight:400;text-decoration:underline}
.topbar .cart{left:1010px;top:11px}

/* hero */
.hero{left:0;top:40px;width:1200px;height:678px;background:linear-gradient(180deg,#5b6a6c 0%,#7f8b89 14%,#6e716b 26%,#4a443f 45%,#3a332f 70%,#2c2724 100%)}
.navband{left:0;top:40px;width:1200px;height:103px;background:rgba(40,48,52,0.35)}
.brand{left:171px;top:68px;display:flex;align-items:center;gap:12px;font-family:"Raleway",Arial,sans-serif;font-size:34px;font-weight:400;color:var(--white)}
.brand .dot{width:30px;height:30px;border:2px solid var(--white);border-radius:50%}
.mainnav{left:497px;top:88px;display:flex;gap:22px;font-family:"Montserrat",Arial,sans-serif;font-size:11.5px;font-weight:700;color:var(--white)}
.mainnav .active{position:relative}
.mainnav .active:after{content:"";position:absolute;left:0;right:0;top:28px;height:2px;background:var(--white)}

.seal{left:423px;top:174px;width:356px;height:356px;border-radius:50%;border:2px dashed rgba(230,170,110,0.9);padding:8px}
.seal-inner{width:100%;height:100%;border-radius:50%;background:rgba(196,128,72,0.55);position:relative}
.seal-mark{left:50%;top:56px;transform:translateX(-50%);display:flex;flex-direction:column;align-items:center;gap:6px;font-family:"Raleway",Arial,sans-serif;font-size:13px;font-weight:600;color:var(--white);letter-spacing:1px}
.seal-mark .dot{width:46px;height:46px;border:2px solid var(--white);border-radius:50%}
.seal-list{left:66px;top:160px;list-style:none;font-family:"Montserrat",Arial,sans-serif;font-size:12.5px;font-weight:700;letter-spacing:1px;color:var(--white)}
.seal-list li{display:flex;align-items:center;gap:14px;height:31px}

/* sections */
.section-title{left:0;width:1200px;text-align:center;font-family:"Montserrat",Arial,sans-serif;font-size:13px;font-weight:600;letter-spacing:2px;color:var(--ink)}
.section-title span{color:var(--gold)}

.product{top:903px;width:90px;height:154px}
.product .shadow{position:absolute;left:-15px;bottom:-8px;width:120px;height:14px;border-radius:50%;background:radial-gradient(closest-side,rgba(0,0,0,0.18),transparent)}
.bottle{position:absolute;bottom:0;left:50%;transform:translateX(-50%)}
.product-info{left:394px;top:1073px;width:200px;text-align:center}
.product-info .name{font-family:"Montserrat",Arial,sans-serif;font-size:11px;font-weight:700;color:var(--ink)}
.product-info .sub{font-size:10.5px;color:var(--muted);margin-top:4px}
.product-info .price{font-family:"Montserrat",Arial,sans-serif;font-size:12px;font-weight:700;color:var(--gold);margin-top:12px}
.product-info .rule{width:28px;height:2px;background:var(--gold);margin:5px auto 0}
.slider-arrow{top:980px}

.post{position:absolute}
.post .photo{width:100%}
.post .caption{position:absolute;left:0;right:0;height:72px;background:var(--caption);display:flex;align-items:center}
.post .badge{width:62px;height:62px;margin-left:8px;border-radius:50%;background:var(--gold);border:2px solid rgba(255,255,255,0.6);display:flex;flex-direction:column;align-items:center;justify-content:center;font-family:"Montserrat",Arial,sans-serif;font-size:8.5px;font-weight:700;color:var(--white);line-height:1.3}
.post .excerpt{margin-left:22px;font-size:11.5px;line-height:1.75;color:#444}

/* consultation */
.consult{left:0;top:2260px;width:1200px;height:575px;background:linear-gradient(180deg,#8e8885 0%,#a39d99 45%,#b9b4b1 75%,#a7a19c 100%)}
.consult-figure{left:430px;top:2575px;width:380px;height:260px;background:linear-gradient(90deg,#b79a86,#8a6c5c 55%,#3a2c27);border-radius:140px 140px 0 0;opacity:0.55}
.consult-title{left:0;top:2350px;width:1200px;text-align:center;font-family:"Raleway",Arial,sans-serif;font-weight:300;font-size:58px;color:var(--white)}
.consult-sub{left:0;top:2440px;width:1200px;text-align:center;font-family:"Montserrat",Arial,sans-serif;font-size:11px;font-weight:700;letter-spacing:2px;color:var(--white)}
.consult-btn{left:489px;top:2511px;width:221px;height:55px;background:var(--gold);display:flex;align-items:center;justify-content:center;font-family:"Montserrat",Arial,sans-serif;font-size:10.5px;font-weight:700;letter-spacing:1px;color:var(--white)}

/* feature tiles */
.tile{top:2835px;height:444px}
.tile-library{left:0;width:601px;background:linear-gradient(180deg,#3d4446 0%,#59605f 40%,#6b6a62 70%,#3b3d3d 100%)}
.tile-active{left:601px;width:599px;background:linear-gradient(135deg,#d8cfc2 0%,#b8ad9c 40%,#4f6a3f 65%,#a99a86 100%)}
.tile-bar{height:12px;background:var(--white)}
.tile-word{font-family:"Montserrat",Arial,sans-serif;font-weight:700;font-size:74px;letter-spacing:4px;color:var(--white);line-height:92px}

/* footer */
.footer{left:0;top:3279px;width:1200px;height:285px;background:var(--footer);color:#cfcfcf}
.footer .mark{left:216px;top:3324px;width:76px;height:76px;border:2px solid #d9d9d9;border-radius:50%;display:flex;align-items:center;justify-content:center;text-align:center;font-family:"Raleway",Arial,sans-serif;font-size:11px;font-weight:600;color:#eee;line-height:1.2}
.footer .divider{top:3303px;width:1px;height:237px;background:var(--footer-line)}
.footer h4{font-family:"Montserrat",Arial,sans-serif;font-size:15px;font-weight:600;color:var(--white)}
.contact{left:171px;top:3414px;font-size:10px;line-height:1.4}
.contact li{list-style:none;display:flex;gap:14px;align-items:flex-start;height:36px}
.sitemap-links{left:461px;top:3418px;list-style:none;font-size:10px;line-height:24px}
.social{left:658px;top:3418px;display:flex;gap:14px}
.social i{display:block;width:11px;height:11px;border-radius:50%;background:var(--gold)}
.copy{left:658px;top:3450px;font-size:10px;display:flex;gap:6px;align-items:center}
.signup{left:855px;top:3420px;font-size:10px}
.news-field{left:855px;top:3440px;width:171px;height:25px;background:var(--white);border-radius:13px;overflow:hidden}
.news-field .send{position:absolute;right:0;top:0;width:40px;height:25px;background:var(--gold);border-radius:0 13px 13px 0;display:flex;align-items:center;justify-content:center}
</style>
</head>
<body>

<!-- hero -->
<div class="abs hero" role="img" aria-label="Photograph of a woman in a bikini lying on a black sand beach with the sea and a green headland behind"></div>

<div class="abs topbar">
  <div class="abs flag" role="img" aria-label="English language flag"></div>
  <div class="abs lang-caret"></div>
  <div class="abs site-name">Halvessa Rue</div>
  <div class="abs login">Log In</div>
  <div class="abs register">Register</div>
  <svg class="abs cart" width="18" height="16" viewBox="0 0 18 16"><path d="M1 1h3l2 9h9l2-7H5" fill="none" stroke="#fff" stroke-width="1.8"/><circle cx="7" cy="13.5" r="1.5" fill="#fff"/><circle cx="14" cy="13.5" r="1.5" fill="#fff"/></svg>
</div>

<div class="abs navband"></div>
<div class="abs brand"><span>Halvessa</span><span class="dot"></span><span>Rue</span></div>
<nav class="abs mainnav">
  <span class="active">Home</span><span>Face</span><span>Body</span><span>Hair Care</span><span>Skin Conditions</span><span>Doctor Consultation</span><span>Library</span>
</nav>

<div class="abs seal">
  <div class="seal-inner">
    <div class="abs seal-mark"><span class="dot"></span><span>HALVESSA RUE</span></div>
    <ul class="abs seal-list">
      <li><svg width="13" height="11" viewBox="0 0 13 11"><path d="M1 6l4 4 7-9" fill="none" stroke="#fff" stroke-width="2.4"/></svg>SKIN CARE</li>
      <li><svg width="13" height="11" viewBox="0 0 13 11"><path d="M1 6l4 4 7-9" fill="none" stroke="#fff" stroke-width="2.4"/></svg>DOCTOR FORMULATED</li>
      <li><svg width="13" height="11" viewBox="0 0 13 11"><path d="M1 6l4 4 7-9" fill="none" stroke="#fff" stroke-width="2.4"/></svg>FRESHLY HANDMADE</li>
      <li><svg width="13" height="11" viewBox="0 0 13 11"><path d="M1 6l4 4 7-9" fill="none" stroke="#fff" stroke-width="2.4"/></svg>REGISTERED PHARMACY</li>
    </ul>
  </div>
</div>

<!-- products -->
<div class="abs section-title" style="top:815px">OUR <span>PRODUCTS</span></div>

<svg class="abs slider-arrow" style="left:172px" width="16" height="40" viewBox="0 0 16 40"><path d="M14 2L2 20l12 18" fill="none" stroke="#c9c9c9" stroke-width="2"/></svg>
<svg class="abs slider-arrow" style="left:1010px" width="16" height="40" viewBox="0 0 16 40"><path d="M2 2l12 18L2 38" fill="none" stroke="#c9c9c9" stroke-width="2"/></svg>

<div class="abs product" style="left:233px"><div class="shadow"></div><div class="bottle" role="img" aria-label="Amber dropper bottle of serum" style="width:44px;height:140px;background:linear-gradient(180deg,#1b1b1b 0 30%,#6b3512 30%,#a35a22 60%,#5a2b0d);border-radius:6px 6px 4px 4px"></div></div>
<div class="abs product" style="left:449px"><div class="shadow"></div><div class="bottle" role="img" aria-label="Black pump bottle of lotion" style="width:46px;height:154px;background:linear-gradient(90deg,#111,#333 50%,#111);border-radius:6px"></div></div>
<div class="abs product" style="left:661px"><div class="shadow"></div><div class="bottle" role="img" aria-label="Brown glass jar of cream with a black lid" style="width:96px;height:100px;background:linear-gradient(180deg,#222 0 26%,#e6dccb 26% 80%,#5a3416 80%);border-radius:6px"></div></div>
<div class="abs product" style="left:882px"><div class="shadow"></div><div class="bottle" role="img" aria-label="Amber spray bottle of toner" style="width:46px;height:150px;background:linear-gradient(180deg,#222 0 22%,#c76a1d 22%,#e08c3c 55%,#9b4c12);border-radius:6px"></div></div>

<div class="abs product-info">
  <div class="name">Lorem Ipsum</div>
  <div class="sub">Lorem Ipsum Dolor Sit</div>
  <div class="price">$48</div>
  <div class="rule"></div>
</div>

<!-- blog -->
<div class="abs section-title" style="top:1238px">OUR <span>BLOG</span></div>

<article class="post" style="left:171px;top:1354px;width:383px">
  <div class="photo" role="img" aria-label="Photograph of a blonde woman in a grey sweater in a dry meadow" style="height:214px;background:linear-gradient(135deg,#b49a7c,#8e7256 50%,#d9c3a4)"></div>
  <div class="caption" style="top:214px"><div class="badge"><span>21 JUNE</span><span>2016</span></div><p class="excerpt">Lorem ipsum dolor sit amet, consectetur<br>adipiscing elit, sed do eiusmod</p></div>
</article>

<article class="post" style="left:646px;top:1354px;width:380px">
  <div class="photo" role="img" aria-label="Photograph of a smiling woman in a turquoise hat and white top in a garden" style="height:352px;background:linear-gradient(180deg,#9fb47a,#c9d1b6 45%,#9ab3d2 85%)"></div>
  <div class="caption" style="top:352px"><div class="badge"><span>21 JUNE</span><span>2016</span></div><p class="excerpt">Lorem ipsum dolor sit amet, consectetur<br>adipiscing elit, sed do eiusmod</p></div>
</article>

<article class="post" style="left:171px;top:1734px;width:383px">
  <div class="photo" role="img" aria-label="Portrait photograph of a woman with long curly auburn hair" style="height:357px;background:linear-gradient(135deg,#e9ddd0,#a5704a 45%,#6a3f22 80%)"></div>
  <div class="caption" style="top:357px;height:71px"><div class="badge"><span>21 JUNE</span><span>2016</span></div><p class="excerpt">Lorem ipsum dolor sit amet, consectetur<br>adipiscing elit, sed do eiusmod</p></div>
</article>

<article class="post" style="left:646px;top:1875px;width:380px">
  <div class="photo" role="img" aria-label="Photograph of a dark haired woman beside pink roses" style="height:216px;background:linear-gradient(90deg,#e8e0da,#c9a59a 55%,#e6c4c4)"></div>
  <div class="caption" style="top:216px;height:71px"><div class="badge"><span>21 JUNE</span><span>2016</span></div><p class="excerpt">Lorem ipsum dolor sit amet, consectetur<br>adipiscing elit, sed do eiusmod</p></div>
</article>

<!-- consultation -->
<div class="abs consult" role="img" aria-label="Photograph of a dermatologist examining a patient's face"></div>
<div class="abs consult-figure" role="img" aria-label="Doctor and patient figures"></div>
<h2 class="abs consult-title">Lorem Ipsum Dolor Sit</h2>
<div class="abs consult-sub">LOREM IPSUM DOLOR SIT AMET CONSECTETUR</div>
<div class="abs consult-btn">START YOUR CASE NOW</div>

<!-- feature tiles -->
<div class="abs tile tile-library" role="img" aria-label="Photograph of a library bookcase filled with books"></div>
<div class="abs tile tile-active" role="img" aria-label="Photograph of a green glass bottle with rosemary sprigs and towels"></div>
<div class="abs tile-bar" style="left:119px;top:2924px;width:99px"></div>
<div class="abs tile-word" style="left:113px;top:2966px">LIBRARY</div>
<div class="abs tile-bar" style="left:637px;top:2924px;width:95px"></div>
<div class="abs tile-word" style="left:633px;top:2962px">ACTIVE<br>INGREDIENT</div>

<!-- footer -->
<footer class="abs footer"></footer>
<div class="abs footer mark" style="background:none;width:76px;height:76px">HALVESSA<br>RUE</div>
<ul class="abs contact" style="color:#cfcfcf">
  <li><svg width="14" height="14" viewBox="0 0 14 14"><path d="M3 1l3 3-2 2c1 2 2 3 4 4l2-2 3 3-2 2C6 13 1 8 1 3z" fill="none" stroke="#cfcfcf" stroke-width="1.2"/></svg><span>800-410-7725</span></li>
  <li><svg width="14" height="12" viewBox="0 0 14 12"><rect x="1" y="1" width="12" height="10" fill="none" stroke="#cfcfcf" stroke-width="1.2"/><path d="M1 1l6 5 6-5" fill="none" stroke="#cfcfcf" stroke-width="1.2"/></svg><span>hello@halvessarue.com</span></li>
  <li><svg width="12" height="16" viewBox="0 0 12 16"><path d="M6 15C2 10 1 7 1 5.5a5 5 0 0110 0C11 7 10 10 6 15z" fill="none" stroke="#cfcfcf" stroke-width="1.2"/><circle cx="6" cy="5.5" r="1.8" fill="#cfcfcf"/></svg><span>Harrow Street, Lorem Ipsum<br>21000</span></li>
</ul>
<div class="abs divider footer" style="left:385px;top:3303px;width:1px;height:237px;background:var(--footer-line)"></div>
<div class="abs divider footer" style="left:812px;top:3303px;width:1px;height:237px;background:var(--footer-line)"></div>
<h4 class="abs" style="left:456px;top:3366px;font-family:'Montserrat',Arial,sans-serif;font-size:15px;font-weight:600;color:#fff">Site Map</h4>
<ul class="abs sitemap-links" style="color:#cfcfcf"><li>Philosophy</li><li>Categories</li><li>Customer Care</li><li>News</li></ul>
<h4 class="abs" style="left:658px;top:3366px;font-family:'Montserrat',Arial,sans-serif;font-size:15px;font-weight:600;color:#fff">Folow Us</h4>
<div class="abs social"><i></i><i></i><i></i></div>
<div class="abs copy" style="color:#cfcfcf"><svg width="11" height="11" viewBox="0 0 11 11"><circle cx="5.5" cy="5.5" r="4.5" fill="none" stroke="#cfcfcf"/></svg>2016 Halvessa Rue</div>
<h4 class="abs" style="left:865px;top:3366px;font-family:'Montserrat',Arial,sans-serif;font-size:15px;font-weight:600;color:#fff">Newsletter</h4>
<div class="abs signup" style="color:#cfcfcf">Signup for newsletter</div>
<div class="abs news-field"><div class="send"><svg width="12" height="11" viewBox="0 0 12 11"><path d="M1 5l10-4-3 9-2-4z" fill="#fff"/></svg></div></div>

</body>
</html>
```